Vellum Systemics Buisness Cards

I need a technology focused clean business card for my employees. I have attached out logo to include in the mocks. We're a modern tech consulting firm that drives to interface humanity with technology in a truly cohesive fashion.

```html
<!DOCTYPE html>
<html lang="en">
<head>
<meta charset="utf-8">
<title>Vellum Systemics Business Cards</title>
<link href="https://fonts.googleapis.com/css2?family=Lato:wght@400;700&display=swap" rel="stylesheet">
<style>
  :root {
    --brand-blue: #1e74bd;
    --brand-grey: #7e8083;
    --ink: #1c1c1c;
    --paper: #ffffff;
    --backdrop: #e9eaec;
  }
  * { margin: 0; padding: 0; box-sizing: border-box; }
  html, body { width: 1200px; height: 900px; overflow: hidden; }
  body {
    background: var(--backdrop);
    font-family: "Lato", sans-serif;
    position: relative;
  }
  .card {
    position: absolute;
    left: 250px;
    width: 700px;
    height: 400px;
    overflow: hidden;
    box-shadow: 0 6px 18px rgba(0,0,0,0.18);
  }
  /* Back side */
  .card-back { top: 30px; background: var(--brand-blue); color: var(--paper); }
  .card-back .brand {
    position: absolute; left: 0; right: 0; top: 150px;
    display: flex; align-items: center; justify-content: center; gap: 18px;
  }
  .card-back .brand-dot {
    width: 46px; height: 46px; border-radius: 50%; background: var(--paper);
  }
  .card-back .brand-name {
    font-size: 54px; font-weight: 700; letter-spacing: 0.5px; color: var(--paper);
  }
  .card-back .web {
    position: absolute; left: 0; right: 0; top: 300px; text-align: center;
    font-size: 19px; letter-spacing: 1px;
  }
  /* Front side */
  .card-front { top: 470px; background: var(--paper); }
  .card-front .swoosh { position: absolute; inset: 0; }
  .card-front .brand {
    position: absolute; left: 40px; top: 110px; width: 290px;
    display: flex; align-items: center; gap: 12px;
  }
  .card-front .brand-dot {
    width: 30px; height: 30px; border-radius: 50%; background: var(--brand-blue); flex: none;
  }
  .card-front .brand-name {
    font-size: 30px; font-weight: 700; color: var(--brand-grey); line-height: 1.05;
  }
  .divider {
    position: absolute; left: 355px; top: 60px; width: 2px; height: 175px;
    background: var(--brand-blue);
  }
  .contact {
    position: absolute; left: 385px; top: 62px; color: var(--ink);
    font-size: 17px; line-height: 1.3;
  }
  .contact .name { color: var(--brand-blue); font-size: 26px; font-weight: 700; line-height: 1.1; }
  .contact .role { margin-bottom: 10px; }
  .contact .row { display: flex; align-items: center; gap: 8px; }
  .contact .row svg { width: 14px; height: 14px; fill: var(--brand-blue); flex: none; }
  .contact .address { margin-bottom: 4px; }
  .card-front .web {
    position: absolute; left: 150px; top: 330px;
    color: var(--paper); font-size: 20px; letter-spacing: 1px;
  }
</style>
</head>
<body>

<section class="card card-back">
  <div class="brand">
    <span class="brand-dot"></span>
    <span class="brand-name">Vellum Systemics</span>
  </div>
  <p class="web">www.vellumsys.com</p>
</section>

<section class="card card-front">
  <svg class="swoosh" viewBox="0 0 700 400" preserveAspectRatio="none" aria-hidden="true">
    <path d="M0,245 Q380,262 700,355 L700,378 Q380,284 0,258 Z" fill="var(--brand-grey)"/>
    <path d="M0,266 Q380,292 700,388 L700,400 L0,400 Z" fill="var(--brand-blue)"/>
  </svg>

  <div class="brand">
    <span class="brand-dot"></span>
    <span class="brand-name">Vellum Systemics</span>
  </div>

  <div class="divider"></div>

  <div class="contact">
    <p class="name">Daniel Okafor</p>
    <p class="role">Manager</p>
    <p class="address">418 Alder Row<br>Houston, TX 77041</p>
    <p class="row">
      <svg viewBox="0 0 24 24"><path d="M6.6 10.8a15.1 15.1 0 0 0 6.6 6.6l2.2-2.2a1 1 0 0 1 1-.25 11.4 11.4 0 0 0 3.6.57 1 1 0 0 1 1 1V20a1 1 0 0 1-1 1A17 17 0 0 1 3 4a1 1 0 0 1 1-1h3.5a1 1 0 0 1 1 1c0 1.25.2 2.45.57 3.57a1 1 0 0 1-.25 1z"/></svg>
      512 555 0142
    </p>
    <p class="row">
      <svg viewBox="0 0 24 24"><path d="M7 1h10a2 2 0 0 1 2 2v18a2 2 0 0 1-2 2H7a2 2 0 0 1-2-2V3a2 2 0 0 1 2-2zm0 3v14h10V4zm5 15.5a1 1 0 1 0 0 2 1 1 0 0 0 0-2z"/></svg>
      512 555 0143
    </p>
    <p class="row">
      <svg viewBox="0 0 24 24"><path d="M2 5h20v14H2zm2 2v.5l8 5 8-5V7zm0 2.8V17h16V9.8l-8 5z"/></svg>
      info@vellumsys.com
    </p>
  </div>

  <p class="web">www.vellumsys.com</p>
</section>

</body>
</html>
```